Energy drink company looking for a complete can design

Design an energy drink can label using an established trademarked logo along with mandatory nutrition and ingredients table.
We would like to see 3 versions or samples to judge:
1. can design over a black background - called dark color version
2. can design over a white background - called light color version
3. can design over a grey/silver background - called balanced color version

Target Market(s)

USA

Requirements
Must have
• the phrase "yes kelvora energy drink" "yes kelvora" and "ALL Natural Libido Enhancing energy drink" must be on the can somewhere

```html
<!DOCTYPE html>
<html lang="en">
<head>
<meta charset="utf-8">
<title>yes kelvora energy drink – can label</title>
<link rel="stylesheet" href="https://fonts.googleapis.com/css2?family=Oswald:wght@400;700&family=Roboto:wght@400;700&family=Open+Sans:wght@400;600&display=swap">
<style>
  :root {
    --bg-light: #4b4b4d;
    --bg-dark: #2c2c2e;
    --white: #ffffff;
    --soft-white: #e6e6e6;
    --muted: #b9b9b9;
    --yellow: #f7c515;
    --orange: #f0982c;
    --fruit-light: #f9d34a;
    --fruit-dark: #d98a14;
    --rule: rgba(255,255,255,0.85);
  }
  * { margin: 0; padding: 0; box-sizing: border-box; }
  html, body { width: 1200px; height: 846px; overflow: hidden; background: var(--bg-dark); }
  .can-label {
    position: relative; width: 1200px; height: 846px; overflow: hidden;
    background: radial-gradient(ellipse at 45% 45%, var(--bg-light) 0%, #3c3c3e 55%, var(--bg-dark) 100%);
    color: var(--white);
  }
  .fruit-art {
    position: absolute; left: 150px; top: 72px; width: 262px; height: 470px;
    border-radius: 46% 46% 42% 42%;
    background: radial-gradient(ellipse at 50% 35%, var(--fruit-light) 0%, #f1b32a 50%, var(--fruit-dark) 100%);
  }
  .fruit-photo { position: absolute; background: radial-gradient(circle at 40% 40%, var(--fruit-light), var(--fruit-dark)); opacity: 0.9; }
  .fruit-photo--bottom-left { left: -40px; top: 630px; width: 240px; height: 260px; border-radius: 50%; }
  .fruit-photo--bottom-right { left: 1050px; top: 580px; width: 230px; height: 300px; border-radius: 50%; }
  .fruit-photo--top { left: 470px; top: -40px; width: 200px; height: 84px; border-radius: 50%; opacity: 0.75; }

  .brand-name {
    position: absolute; left: 86px; top: 512px; width: 360px; text-align: center;
    font-family: "Oswald", sans-serif; font-weight: 400; font-size: 66px; line-height: 1;
    color: var(--orange);
  }
  .tagline {
    position: absolute; left: 172px; top: 663px; width: 240px; text-align: center;
    font-family: "Roboto", sans-serif; font-weight: 700; font-size: 12px; line-height: 1.25;
    letter-spacing: 0.3px; text-transform: uppercase;
  }
  .vertical-title {
    position: absolute; font-family: "Oswald", sans-serif; font-weight: 700;
    transform-origin: left top; white-space: nowrap; line-height: 1;
  }
  .vertical-title--product { left: 566px; top: 706px; transform: rotate(-90deg); font-size: 44px; color: var(--white); }
  .vertical-title--brand { left: 1062px; top: 462px; transform: rotate(-90deg); font-size: 48px; color: var(--yellow); }

  .nutrition-facts {
    position: absolute; left: 732px; top: 42px; width: 236px; padding: 2px 4px 4px;
    border: 1px solid rgba(255,255,255,0.35);
    font-family: "Roboto", sans-serif; color: var(--white);
  }
  .nutrition-facts__title { font-weight: 700; font-size: 31px; line-height: 1.05; letter-spacing: -0.3px; }
  .nutrition-facts__title span { color: var(--yellow); }
  .nutrition-facts__row { display: flex; justify-content: space-between; font-size: 10px; line-height: 15.2px; border-top: 0.6px solid var(--rule); }
  .nutrition-facts__row--first { border-top: 1.2px solid var(--rule); }
  .nutrition-facts__row--indent { padding-left: 12px; }
  .nutrition-facts__row--indent2 { padding-left: 24px; }
  .nutrition-facts__row--muted { color: var(--muted); }
  .nutrition-facts__serving { display: flex; justify-content: space-between; font-weight: 700; font-size: 12.5px; margin-top: 3px; }
  .nutrition-facts__bar { height: 8px; background: var(--white); margin: 4px 0 3px; }
  .nutrition-facts__bar--medium { height: 5px; margin: 2px 0 0; }
  .nutrition-facts__amount { font-size: 9.5px; font-weight: 700; }
  .nutrition-facts__calories { display: flex; justify-content: space-between; align-items: baseline; font-weight: 700; font-size: 20px; line-height: 1; }
  .nutrition-facts__calories strong { font-size: 28px; }
  .nutrition-facts__dv { text-align: right; font-size: 8.5px; line-height: 13px; border-top: 1.2px solid var(--rule); }
  .nutrition-facts__footnote { font-size: 7.2px; line-height: 1.25; color: var(--muted); margin-top: 4px; border-top: 1.2px solid var(--rule); padding-top: 3px; }
  b { font-weight: 700; }

  .label-copy {
    position: absolute; left: 640px; top: 594px; width: 490px;
    font-family: "Open Sans", sans-serif; font-size: 13.2px; line-height: 21px; color: var(--soft-white);
  }
  .label-copy__line { display: flex; }
  .label-copy__key { width: 86px; flex: none; text-align: right; padding-right: 8px; }
  .label-copy .hl { color: var(--yellow); }
  .label-copy .em { color: var(--white); font-weight: 600; }
</style>
</head>
<body>
<main class="can-label">
  <div class="fruit-photo fruit-photo--top" role="img" aria-label="Pineapple slice photograph"></div>
  <div class="fruit-photo fruit-photo--bottom-left" role="img" aria-label="Splashing pineapple slices photograph"></div>
  <div class="fruit-photo fruit-photo--bottom-right" role="img" aria-label="Pineapple chunks photograph"></div>

  <div class="fruit-art" role="img" aria-label="Illustration of a juicy pineapple with a slice and juice splash"></div>
  <div class="brand-name">yes kelvora</div>
  <p class="tagline">All natural libido<br>enhancing energy drink</p>

  <div class="vertical-title vertical-title--product">yes kelvora energy drink</div>
  <div class="vertical-title vertical-title--brand">yes kelvora</div>

  <section class="nutrition-facts" aria-label="Nutrition Facts">
    <h2 class="nutrition-facts__title"><span>N</span>utrition Facts</h2>
    <div class="nutrition-facts__serving"><span>Serving size</span><span>12 fl oz (355 mL)</span></div>
    <div class="nutrition-facts__bar"></div>
    <div class="nutrition-facts__amount">Amount per serving</div>
    <div class="nutrition-facts__calories"><span>Calories</span><strong>90</strong></div>
    <div class="nutrition-facts__bar nutrition-facts__bar--medium"></div>
    <div class="nutrition-facts__dv">% Daily Value*</div>
    <div class="nutrition-facts__row nutrition-facts__row--first"><span><b>Total Fat</b> 0g</span><span>0%</span></div>
    <div class="nutrition-facts__row nutrition-facts__row--indent"><span>Saturated Fat 0g</span><span>0%</span></div>
    <div class="nutrition-facts__row nutrition-facts__row--indent"><span>Trans Fat 0g</span><span></span></div>
    <div class="nutrition-facts__row"><span><b>Cholesterol</b> 0mg</span><span>0%</span></div>
    <div class="nutrition-facts__row"><span><b>Sodium</b> 5mg</span><span>0%</span></div>
    <div class="nutrition-facts__row"><span><b>Total Carbohydrate</b> 21g</span><span>8%</span></div>
    <div class="nutrition-facts__row nutrition-facts__row--indent"><span>Dietary Fiber 0g</span><span>0%</span></div>
    <div class="nutrition-facts__row nutrition-facts__row--indent"><span>Total Sugars 18g</span><span></span></div>
    <div class="nutrition-facts__row nutrition-facts__row--indent2"><span>Includes 0g Added Sugars</span><span>0%</span></div>
    <div class="nutrition-facts__row"><span><b>Protein</b> 0g</span><span></span></div>
    <div class="nutrition-facts__bar nutrition-facts__bar--medium"></div>
    <div class="nutrition-facts__row nutrition-facts__row--first nutrition-facts__row--muted"><span>Vitamin D 0mcg</span><span>0%</span></div>
    <div class="nutrition-facts__row nutrition-facts__row--muted"><span>Calcium 18mg</span><span>2%</span></div>
    <div class="nutrition-facts__row nutrition-facts__row--muted"><span>Iron 0mg</span><span>0%</span></div>
    <div class="nutrition-facts__row nutrition-facts__row--muted"><span>Potassium 238mg</span><span>6%</span></div>
    <div class="nutrition-facts__row nutrition-facts__row--muted"><span>Vitamin C 138mg</span><span>150%</span></div>
    <div class="nutrition-facts__row nutrition-facts__row--muted"><span>Niacin 24mg</span><span>150%</span></div>
    <div class="nutrition-facts__row nutrition-facts__row--muted"><span>Vitamin B<sub>6</sub> 2.6mg</span><span>150%</span></div>
    <div class="nutrition-facts__row nutrition-facts__row--muted"><span>Vitamin B<sub>12</sub> 3.6mcg</span><span>150%</span></div>
    <div class="nutrition-facts__row nutrition-facts__row--muted"><span>Pantothenic Acid 7mg</span><span>140%</span></div>
    <div class="nutrition-facts__row nutrition-facts__row--muted"><span>Zinc 6mg</span><span>50%</span></div>
    <p class="nutrition-facts__footnote">*The % Daily Value tells you how much a nutrient in a serving of food contributes to a daily diet. 2,000 calories a day is used for general nutrition advice.</p>
  </section>

  <section class="label-copy">
    <div class="label-copy__line"><span class="label-copy__key">Allergens:</span><span>None</span></div>
    <div class="label-copy__line"><span class="label-copy__key">Ingredients:</span>
      <span>Filtered Water, Organic Peach Juice <span class="em">Concentrate</span>, Organic White Grape Juice Concentrate, Organic <span class="em">Pear</span> Juice Concentrate, Organic Pineapple Juice <span class="em">Concentrate</span>, <span class="hl">Organic Natural Flavors</span>, Horny Goat Weed <span class="em">Extract</span>, <span class="em">Citric Acid</span>, <span class="hl">L-Arginine</span>, Taurine, Maca Root <span class="em">Extract</span>, <span class="hl">Ascorbic Acid</span>, <span class="hl">Natural</span> Caffeine from Green Tea, <span class="em">Panax Ginseng</span>, <span class="hl">Organic Monk Fruit</span>, <span class="em">Gingko Biloba</span>, Stevia Reb M, <span class="hl">Niacinamide</span>, <span class="hl">Zinc Citrate</span>, <span class="hl">Calcium</span> Pantothenate, <span class="em">Pyridoxine</span> <span class="hl">Hydrochloride</span>, <span class="hl">Cyanocobalamin</span></span>
    </div>
  </section>
</main>
</body>
</html>
```